Fun Feminine Redesign Product Landing Page

This is our current product page
https://dovelmintery.com/product/coffee-substitute/

I like the overall feel of this but it needs to pop more. I love the pink an we are in the process of having illustrations made for the how to section.

Examples with more pop
https://www.brambleoven.com/products/chicken-bone-broth?shipping=8
https://pawtonmeal.com/products/lamb-turkey-kibble-grain-free

Target Market(s)

females 24-44

Number of Pages Required

1 page

Colors
0094D4
00A9DD
6FCCEA
C7EBF8
E9F6FB
00AB8E
00BBA5
67D7C9
C6EFE9
E9F9F6
FFC000
F8CF3A
FAE287
FDF2CF
FEFAEE
E54698
E96AAD
F1A4CE
F9D9EA
FCEFF6

Requirements
Must have
• Fresh, clean, feminine and unique

```html
<!DOCTYPE html>
<html lang="en">
<head>
<meta charset="utf-8">
<title>Dovel Mintery – Original Coffee Substitute</title>
<link href="https://fonts.googleapis.com/css2?family=Lora:wght@400;500&family=Jost:wght@400;500;600&display=swap" rel="stylesheet">
<style>
:root{
  --cream:#fdf2cf;
  --cream-soft:#fefaee;
  --hero:#fae287;
  --hero-soft:#fce9a9;
  --gold:#ffc000;
  --amber:#f8a300;
  --navy:#1f2a5c;
  --ink:#2b2b2b;
  --muted:#555;
  --pink:#e96aad;
  --pink-deep:#e54698;
  --pink-soft:#f9d9ea;
  --pink-pale:#fceff6;
  --card:#f4eed8;
  --green:#3aa35b;
}
*{box-sizing:border-box;margin:0;padding:0}
html,body{width:1200px;height:5396px;overflow:hidden}
body{font-family:"Jost",sans-serif;color:var(--ink);background:#fff;position:relative;font-size:13px}
.abs{position:absolute}
.serif{font-family:"Lora",serif}
.ph{position:absolute;border-radius:2px}
.stars{color:var(--gold);letter-spacing:2px}

/* header */
.site-header{position:absolute;left:0;top:0;width:1200px;height:113px;background:#fff}
.brand{position:absolute;left:130px;top:36px;font-family:"Lora",serif;font-size:22px;line-height:24px;color:var(--amber)}
.nav{position:absolute;left:588px;top:44px;display:flex;gap:34px;font-size:16px;color:#444}
.cart{position:absolute;left:1036px;top:36px;width:33px;height:33px;background:var(--navy);border-radius:4px}
.cart:after{content:"0";position:absolute;right:-5px;top:-5px;width:13px;height:13px;border-radius:50%;background:var(--pink);color:#fff;font-size:9px;text-align:center;line-height:13px}

/* hero */
.hero{position:absolute;left:0;top:113px;width:1200px;height:658px;background:linear-gradient(180deg,var(--hero-soft),var(--hero))}
.hero-main{left:130px;top:42px;width:470px;height:467px;background:linear-gradient(135deg,#1f8f8c,#12706f)}
.thumb{top:522px;width:110px;height:84px;background:#f5f5f5;border:1px solid #ddd}
.buy{left:643px;top:0;width:440px}
.buy .rating{position:absolute;top:40px;font-size:11px}
.buy h1{position:absolute;top:62px;font-family:"Lora",serif;font-weight:400;font-size:25px;white-space:nowrap}
.buy p{position:absolute;font-size:12.5px;line-height:19px;color:#444;width:410px}
.ingredients{position:absolute;top:255px;width:284px;height:114px;background:var(--cream-soft);padding:12px 16px;font-size:12px;line-height:22px}
.ingredients li{list-style:none}
.ingredients .item:before{content:"✔";color:var(--amber);margin-right:8px}
.ingredients .note{font-size:9px;color:#666;margin-left:6px;line-height:16px}
.price{position:absolute;top:392px;font-size:30px;line-height:36px}
.sub{position:absolute;top:432px;font-size:12px;color:#555}
.size-label{position:absolute;top:466px;font-size:12px}
.size{position:absolute;top:490px;height:36px;padding:0 14px;background:var(--gold);border-radius:2px;font-size:12px;line-height:36px;color:#4a3a00}
.qty{position:absolute;top:553px;left:0;width:135px;height:48px;background:#fff;border:1px solid #ccc;padding:0 16px;line-height:46px;font-size:14px}
.add{position:absolute;top:553px;left:158px;width:145px;height:48px;background:var(--amber);color:#fff;text-align:center;line-height:48px;font-weight:600;font-size:15px}

/* section titles */
.dot{position:absolute;width:12px;height:16px;border-radius:50%;background:var(--pink)}
.title{position:absolute;width:1200px;left:0;text-align:center;font-family:"Lora",serif;font-weight:400;font-size:23px}

/* how to */
.step-img{top:907px;width:304px;height:310px;background:linear-gradient(160deg,#fdf2cf,#fcefd9)}
.step-name{top:1248px;width:304px;text-align:center;font-family:"Lora",serif;font-size:18px}
.step-text{top:1284px;width:304px;text-align:center;font-size:13px;line-height:19px;color:#444;padding:0 30px}
.tip{left:330px;top:1400px;width:540px;height:30px;background:var(--hero);text-align:center;line-height:30px;font-size:12.5px;border-radius:2px}
.badge{top:1466px;width:82px;height:82px;border-radius:50%;border:5px solid var(--navy);background:#fff}

/* reasons */
.reasons{left:0;top:1644px;width:1200px;height:450px}
.reason-icon{top:1759px;width:112px;height:112px;border-radius:50%;background:var(--amber)}
.reason-icon svg{position:absolute;left:28px;top:28px}
.reason-h{top:1900px;width:300px;text-align:center;font-size:15px;font-weight:500}
.reason-t{top:1932px;width:300px;text-align:center;font-size:12.5px;line-height:19px;color:#444;padding:0 18px}

/* did you know */
.fact{left:130px;width:408px;border:1px solid #ddd;background:#fff;padding:0 30px 0 48px;display:flex;align-items:center;font-size:12.5px;line-height:18px;color:#333}
.fact:before{content:"";position:absolute;left:16px;width:16px;height:16px;border-radius:50%;background:var(--amber)}
.fact:after{content:"✓";position:absolute;left:20px;color:#fff;font-size:10px}

/* reviews */
.reviews{left:0;top:2659px;width:1200px;height:1498px;background:var(--cream-soft)}
.btn-out{top:2852px;height:34px;border:2px solid var(--amber);background:#fff;font-size:11.5px;line-height:30px;padding:0 16px}
.tabs{left:130px;top:2937px;width:938px;height:30px;border-bottom:1px solid #ddd;font-size:12.5px}
.tabs span{position:absolute;top:4px}
.sort{right:0;top:-4px;width:100px;height:30px;background:#ece7d8;font-size:12px;line-height:30px;padding-left:12px}
.review-date{left:960px;width:108px;text-align:right;font-size:10.5px;color:#555}
.avatar{left:158px;width:60px;height:60px;border-radius:50%;background:#ece4cf;text-align:center;line-height:60px;font-family:"Lora",serif;color:#777}
.reviewer{left:122px;width:134px;text-align:center;font-size:11px;line-height:25px;white-space:nowrap}
.reviewer .v{color:var(--green);font-size:10px}
.review-box{left:310px;width:758px;background:var(--card);padding:22px 44px}
.review-box h3{font-family:"Lora",serif;font-weight:400;font-size:17px;margin-bottom:10px}
.review-box p{font-size:12px;line-height:19px;color:#333}
.review-foot{left:310px;width:758px;font-size:10.5px;color:#444}
.review-foot .right{position:absolute;right:0;top:0}
.page{top:4086px;width:26px;height:26px;border-radius:50%;border:1px solid #bbb;text-align:center;line-height:24px;font-size:11px;background:#fff}

/* related */
.product{top:4301px;width:226px;height:457px;background:#fff;box-shadow:0 2px 10px rgba(0,0,0,.08)}
.product .img{position:absolute;left:0;top:0;width:226px;height:238px}
.product h4{position:absolute;left:20px;top:270px;width:190px;font-family:"Lora",serif;font-weight:400;font-size:13.5px;line-height:19px}
.product .st{position:absolute;left:20px;top:318px;font-size:11px}
.product .st em{font-style:normal;color:#555;font-size:9px;margin-left:4px}
.product .pr{position:absolute;left:20px;top:348px;font-size:13px}
.product .cta{position:absolute;left:20px;top:394px;width:94px;height:32px;background:var(--amber);color:#fff;font-size:10px;text-align:center;line-height:32px}

/* footer */
.site-footer{left:0;top:4800px;width:1200px;height:560px;background:var(--navy);color:#fff}
.f-h{font-family:"Lora",serif;font-size:19px;color:var(--pink)}
.f-links{font-size:13.5px;line-height:31px}
.f-input{left:777px;width:322px;height:30px;background:#fff;border-radius:3px;font-size:9px;color:#888;padding:6px 8px}
.send{left:777px;top:5057px;width:322px;height:36px;background:var(--pink);color:#fff;text-align:center;line-height:36px;font-size:14px;border-radius:3px}
.soc{top:5137px;width:16px;height:16px;border-radius:50%;background:#fff}
.promo{left:0;top:5360px;width:1200px;height:36px;background:var(--pink);color:#fff;text-align:center;line-height:36px;font-size:12.5px}
</style>
</head>
<body>

<header class="site-header">
  <div class="brand">Dovel<br>Mintery</div>
  <nav class="nav"><span>Learn ▾</span><span>About</span><span>Shop</span><span>Contact</span><span>Account Login</span></nav>
  <div class="cart"></div>
</header>

<section class="hero">
  <div class="ph hero-main" role="img" aria-label="Hands holding a cup of coffee substitute beside the product pouch on a teal background"></div>
  <div class="ph thumb" style="left:130px;background:#1f8f8c" role="img" aria-label="Thumbnail of product in hands"></div>
  <div class="ph thumb" style="left:249px" role="img" aria-label="Thumbnail of product pouch"></div>
  <div class="ph thumb" style="left:369px" role="img" aria-label="Thumbnail of nutrition label"></div>
  <div class="ph thumb" style="left:490px" role="img" aria-label="Thumbnail of product pouch"></div>

  <div class="abs buy">
    <div class="rating"><span class="stars">★★★★★</span> 13 reviews</div>
    <h1>Original Coffee Substitute</h1>
    <p style="top:115px">The blend that started it all… Original Dovel Mintery will become your go-to beverage when you're trying to replace that classic cup of joe.</p>
    <p style="top:174px">It has a gentle flavor – not burnt, never acidic, it has just the right welcome tinge of bitterness.</p>
    <p style="top:234px;font-weight:500">Three organic ingredients – no extra additives:</p>
    <ul class="ingredients">
      <li class="item">Organic Roasted Chicory Root</li>
      <li class="item">Organic Roasted Carob Powder</li>
      <li class="item">Organic Roasted Dandelion Powder</li>
      <li class="note">^Really, that's the full ingredient list!</li>
    </ul>
    <div class="price">$15.00 – $28.00</div>
    <div class="sub">or from $12.00 – $22.40 / month</div>
    <div class="size-label">Size</div>
    <div class="size" style="left:0">4 oz ( 15 Savings)</div>
    <div class="size" style="left:165px">8 oz ( 30 Savings)</div>
    <div class="qty">1 <span style="float:right;font-size:10px">▼</span></div>
    <div class="add">Add to Cart</div>
  </div>
</section>

<!-- how to -->
<div class="dot" style="left:594px;top:822px"></div>
<h2 class="title" style="top:846px">How to make a perfect cup</h2>
<div class="ph step-img" style="left:130px" role="img" aria-label="Illustration of a tea bag being placed in a glass cup"></div>
<div class="ph step-img" style="left:448px" role="img" aria-label="Illustration of hot water pouring into the cup"></div>
<div class="ph step-img" style="left:764px" role="img" aria-label="Illustration of the brew steeping light and dark"></div>
<div class="abs step-name" style="left:130px">1. Measure</div>
<div class="abs step-name" style="left:448px">2. Prep</div>
<div class="abs step-name" style="left:764px">3. Steep</div>
<div class="abs step-text" style="left:130px">Place 1 tsp of Dovel Coffee Substitute in a Coffee press or single use drip bags. For a Darker brew increase to 2 tsp.</div>
<div class="abs step-text" style="left:448px">Add 3/4 cup (6oz) of hot water.</div>
<div class="abs step-text" style="left:764px">For a light brew, let steep for up to 60 seconds. For a dark brew, let steep for up to 2 minutes.</div>
<div class="abs tip">*Want a stronger brew? Let it steep longer, OR use a higher ratio of powder to water.</div>
<div class="abs badge" style="left:130px"></div>
<div class="abs badge" style="left:250px"></div>
<div class="abs badge" style="left:371px"></div>
<div class="abs badge" style="left:492px"></div>
<div class="abs badge" style="left:613px"></div>
<div class="abs badge" style="left:734px"></div>
<div class="abs badge" style="left:855px"></div>
<div class="abs badge" style="left:986px"></div>

<!-- reasons -->
<svg class="abs reasons" width="1200" height="450" viewBox="0 0 1200 450"><path d="M0 20 Q600 -20 1200 20 V430 Q600 470 0 430 Z" fill="#fdf2cf"/></svg>
<div class="dot" style="left:594px;top:1655px"></div>
<h2 class="title" style="top:1682px">Pour on the reasons you'll love it:</h2>
<div class="abs reason-icon" style="left:166px"><svg width="56" height="56" viewBox="0 0 56 56" fill="none" stroke="#fff" stroke-width="3"><path d="M28 4 C8 20 8 44 28 52 C48 44 48 20 28 4Z"/><path d="M28 10 V52"/></svg></div>
<div class="abs reason-icon" style="left:544px"><svg width="56" height="56" viewBox="0 0 56 56" fill="none" stroke="#fff" stroke-width="4"><path d="M12 6 H44 M12 50 H44 M16 6 C16 24 40 32 40 50 M40 6 C40 24 16 32 16 50"/></svg></div>
<div class="abs reason-icon" style="left:890px"><svg width="56" height="56" viewBox="0 0 56 56" fill="none" stroke="#fff" stroke-width="4"><path d="M28 48 L8 28 A11 11 0 0 1 28 14 A11 11 0 0 1 48 28 Z"/></svg></div>
<div class="abs reason-h" style="left:72px">None of the Junk</div>
<div class="abs reason-h" style="left:450px">Minerals Galore</div>
<div class="abs reason-h" style="left:796px">Good for the Gut</div>
<div class="abs reason-t" style="left:72px">No artificial (or even those mysterious "natural") flavors!</div>
<div class="abs reason-t" style="left:450px">Toast to your health because our coffee substitutes are rich with calcium, copper, magnesium, selenium, zinc, and more.</div>
<div class="abs reason-t" style="left:796px">Chicory, Carob, and Dandelion are naturally great prebiotics! Both Chicory and Dandelion boast inulin, a great soluble dietary fiber that helps sustain healthy gut bacteria.</div>

<!-- did you know -->
<div class="dot" style="left:310px;top:2163px"></div>
<h2 class="abs serif" style="left:130px;top:2190px;width:378px;text-align:center;font-weight:400;font-size:22px">Did you know?</h2>
<div class="abs fact" style="top:2261px;height:84px">Chicory root's components have been found to work as antioxidants and anti-inflammatories.</div>
<div class="abs fact" style="top:2362px;height:84px">Carob has twice the calcium of cocoa.</div>
<div class="abs fact" style="top:2462px;height:97px">Dandelion contains both beta-carotene, and polyphenols which work against oxidative stress in your body.</div>
<div class="ph" style="left:584px;top:2160px;width:482px;height:437px;background:linear-gradient(150deg,var(--pink-pale),var(--pink-soft))" role="img" aria-label="Hand holding a latte on a wooden board beside an orange product pouch"></div>

<!-- reviews -->
<div class="abs reviews"></div>
<div class="dot" style="left:594px;top:2700px"></div>
<h2 class="title" style="top:2728px">Read Our Reviews</h2>
<div class="abs" style="left:418px;top:2782px;font-size:16px"><span class="stars" style="font-size:34px;letter-spacing:3px">★★★★★</span> <span style="font-size:22px;vertical-align:6px">4.8</span> <span style="font-size:11px;vertical-align:8px;margin-left:6px">Based on 13 Reviews</span></div>
<div class="abs btn-out" style="left:456px">▢ Ask a Question</div>
<div class="abs btn-out" style="left:608px">✎ Write a Review</div>
<div class="abs tabs"><span style="left:0;border-bottom:2px solid var(--ink);padding-bottom:6px">Reviews (13)</span><span style="left:103px">Questions (1)</span><div class="abs sort">Sort <span style="float:right;margin-right:10px;font-size:9px">▼</span></div></div>

<div class="abs review-date" style="top:3000px">01/25/2022</div>
<div class="abs avatar" style="top:3017px">R</div>
<div class="abs reviewer" style="top:3084px">Renna <span class="v">✔ Verified Buyer</span><br>UK<br><span class="stars">★★★★★</span></div>
<div class="abs review-box" style="top:3017px;height:134px"><h3>Very Good</h3><p>Excellent way to Drink a coffee. I'm very happy to try this produce.!</p></div>
<div class="abs review-foot" style="top:3162px">↗ Share<span class="right">Was this helpful? 👍 0 👎 0</span></div>

<div class="abs review-date" style="top:3218px">01/25/2022</div>
<div class="abs avatar" style="top:3235px">R</div>
<div class="abs reviewer" style="top:3303px">Renna <span class="v">✔ Verified Buyer</span><br>UK<br><span class="stars">★★★★★</span></div>
<div class="abs review-box" style="top:3235px;height:136px"><h3>So far so good</h3><p>I've been transitioning from using coffee with their guide and it's taking a bit of tinkering for me.<br>The first time I steeped it too long, then not long enough. I think I've finally got it figured out now, though.<br>It's not exactly like coffee but it hits the spot better than tea for sure!</p></div>
<div class="abs review-foot" style="top:3382px">↗ Share<span class="right">Was this helpful? 👍 0 👎 0</span></div>

<div class="abs review-date" style="top:3430px">01/25/2022</div>
<div class="abs avatar" style="top:3447px">J</div>
<div class="abs reviewer" style="top:3515px">Josie T <span class="v">✔ Verified Buyer</span><br>UK<br><span class="stars">★★★★★</span></div>
<div class="abs review-box" style="top:3447px;height:136px"><h3>I love it!</h3><p>Wonderful! The directions were easy to follow and the coffee tastes delicious!</p></div>
<div class="abs review-foot" style="top:3594px">↗ Share<span class="right">Was this helpful? 👍 0 👎 0</span></div>

<div class="abs review-date" style="top:3640px">01/25/2022</div>
<div class="abs avatar" style="top:3657px">R</div>
<div class="abs reviewer" style="top:3725px">Renna <span class="v">✔ Verified Buyer</span><br>UK<br><span class="stars">★★★★★</span></div>
<div class="abs review-box" style="top:3657px;height:135px"><h3>Love the peppermint mocha</h3><p>I first ordered the Peppermint Mocha and I really like that one! The peppermint mocha has been out of stock, so I ordered the original and it is "okay". Not in love with it but it is AIP compliant and I needed a compliant coffee replacement without added sugar. Thank you for making these and please make more peppermint mocha! I give perming a 5 and original a 3 to 4.</p></div>
<div class="abs review-foot" style="top:3803px">↗ Share<span class="right">Was this helpful? 👍 0 👎 0</span></div>

<div class="abs review-date" style="top:3843px">01/25/2022</div>
<div class="abs avatar" style="top:3860px">J</div>
<div class="abs reviewer" style="top:3928px">Josie T <span class="v">✔ Verified Buyer</span><br>UK<br><span class="stars">★★★★★</span></div>
<div class="abs review-box" style="top:3860px;height:134px"><h3>Best Coffee Substitute I've Found!</h3><p>I've tried a few things to replace coffee in the afternoons, and while this doesn't taste exactly like coffee (and I don't expect it to!) it does have the same bitterness that I love. I really enjoy it :)</p></div>
<div class="abs review-foot" style="top:4006px">↗ Share<span class="right">Was this helpful? 👍 0 👎 0</span></div>

<div class="abs" style="left:522px;top:4090px;font-size:14px">‹</div>
<div class="abs page" style="left:549px">1</div>
<div class="abs page" style="left:586px">2</div>
<div class="abs page" style="left:623px">3</div>
<div class="abs" style="left:668px;top:4090px;font-size:14px">›</div>

<!-- related -->
<div class="dot" style="left:594px;top:4200px"></div>
<h2 class="title" style="top:4235px">Related products</h2>
<div class="abs product" style="left:130px"><div class="img" style="background:linear-gradient(160deg,#e9d6d2,#c9a49b)" role="img" aria-label="Vanilla coffee substitute pouch"></div><h4>"Vanilla" Coffee Substitute (Pre-Order)</h4><div class="st"><span class="stars">★★★★★</span><em>17 Reviews</em></div><div class="pr">$16.00 – $29.00</div><div class="cta">Add to Cart</div></div>
<div class="abs product" style="left:369px"><div class="img" style="background:linear-gradient(160deg,#e8e4e0,#b8b2ac)" role="img" aria-label="Hands holding sample pack pouches"></div><h4>Sample Pack Coffee Substitute – 4 flavors</h4><div class="st"><span class="stars">★★★★★</span><em>17 Reviews</em></div><div class="pr">$37.00</div><div class="cta">Add to Cart</div></div>
<div class="abs product" style="left:607px"><div class="img" style="background:linear-gradient(160deg,#5fb8df,#3a93c4)" role="img" aria-label="Dirty chai pouch with a cup on blue"></div><h4>"Dirty Chai" Coffee Substitute</h4><div class="st"><span class="stars">★★★★★</span><em>17 Reviews</em></div><div class="pr">$17.00 – $32.00</div><div class="cta">Add to Cart</div></div>
<div class="abs product" style="left:844px"><div class="img" style="background:linear-gradient(160deg,#3b4a8a,#1f2a5c)" role="img" aria-label="Mocha pouch with a whipped drink"></div><h4>"Mocha" Coffee Substitute</h4><div class="st"><span class="stars">★★★★★</span><em>17 Reviews</em></div><div class="pr">$15.00 – $28.00</div><div class="cta">Add to Cart</div></div>

<!-- footer -->
<footer class="abs site-footer">
  <div class="abs f-h" style="left:65px;top:60px">Shop</div>
  <div class="abs f-links" style="left:65px;top:96px">Shop All<br>Subscribe<br>Find in Store</div>
  <div class="abs" style="left:65px;top:216px;width:330px;font-size:10.5px;line-height:21px;color:#c8cbe0">Dovel Mintery is your source for autoimmune protocol friendly coffee substitute made of all natural ingredients and an organic chicory, dandelion, and carob base.</div>
  <div class="abs f-h" style="left:421px;top:60px">Learn</div>
  <div class="abs f-links" style="left:421px;top:96px">Shop All<br>Subscribe<br>Accessories<br>Find in Store</div>
  <div class="abs f-h" style="left:421px;top:260px">Partnership</div>
  <div class="abs f-links" style="left:421px;top:296px">Wholesale Info<br>Wholesale Login<br>Affiliate Sign Up</div>
  <div class="abs f-h" style="left:777px;top:60px">Sign up for exclusive discounts</div>
  <div class="abs" style="left:65px;top:510px;font-size:10px">©2022 Dovel Mintery All Rights Reserved.</div>
  <div class="abs" style="left:777px;top:402px;font-size:13px;line-height:24px">hello@dovelmintery.com<br>Privacy Policy</div>
</footer>
<div class="abs f-input" style="top:4901px">Name</div>
<div class="abs f-input" style="top:4938px">Email</div>
<div class="abs f-input" style="top:4975px;height:70px">Message</div>
<div class="abs send">Send</div>
<div class="abs soc" style="left:777px"></div>
<div class="abs soc" style="left:814px"></div>
<div class="abs soc" style="left:851px"></div>
<div class="abs promo">☕ Free Shipping for all US $25+ orders ☕ &nbsp;Dismiss</div>

</body>
</html>
```